Gluten free flour; by MELLOWGRAIN

We are a specialised flour company and this project is to develop packaging for a very niche and upmarket lifestyle gluten free flour in plain and also in wholemeal ( two products and you can choose which one would you like to design and submit for review)

We believe in minimalistic yet easily acceptable Design that STANS OUT and catches the eye of the viewer on a busy shelve in a grocery store.
The product will be sold on our website, through Trovix, through Social Media and also through special campaigns together with Harvest Wellness Alliance of Canada.

We are looking for a stand up bag with zip lock and tear notch size approx. 9 in wide x 13 inch tall x 4 inch gusset .

Our flour produces soft, pliable, moist and fluffy roti and tortillas. (Flour only not finished product).

We only manufacture Gluten free flour and flour related products and do not deal with wheat or wheat related products.
Updates

Website isn't an initial stage URL http://stage.quorvanta.example/mellowgrain Company name : Mellowgrain Inc

Target Market(s)

Canadian East Indian, Canadian-Latin Americans, Caucasian-Canadians and Americans who are gluten free by lifestyle choice or because of Celiac disease or Gluten Intolerance.

Industry/Entity Type

Manufacturing

Logo Text

Mellowgrain

Requirements
Must have
• Prominent "Gluten Free"
Emblems: 100% Organic, 100% Gluten free, Low GI, Vegan, Soy free, dairy free, allergens free, Harvest Wellness Alliance
Roti graphics (picture)
Nice to have
• 0% Saturated Fat only 1% Total fat, Cholesterol Free, Very Low Sodium, Good Source of Dietary Fiber. Weight management. Perfect for Gluten free lifestyle. Organic ingredients
Graphics of grains (Sorghum, Buckwheat, Brown rice, Chickpeas)
Should not have
• Wheat or related to wheat graphics, Anything referring to Gluten. Too busy looking

```html
<!DOCTYPE html>
<html lang="en">
<head>
<meta charset="utf-8">
<title>Mellowgrain Plain Flour – Gluten Free Pack Front</title>
<link href="https://fonts.googleapis.com/css2?family=Libre+Franklin:wght@700;800;900&family=Oswald:wght@500;600&family=Roboto:wght@700&display=swap" rel="stylesheet">
<style>
  :root{
    --frame-dark:#565656;
    --frame-light:#8d8d8d;
    --paper:#ffffff;
    --saffron:#f6b21b;
    --charcoal:#3b3b3b;
    --ink:#2b2b2b;
    --checker:#e9e9e9;
    --grain-gold:#d9b15a;
    --roti-light:#f0d59a;
    --roti-dark:#c99a4e;
  }
  *{margin:0;padding:0;box-sizing:border-box}
  html,body{width:887px;height:1200px;overflow:hidden}
  body{background:var(--frame-dark);position:relative}
  .pack{
    position:absolute;left:59px;top:59px;width:775px;height:1085px;
    background:var(--paper);overflow:hidden;
    outline:4px solid var(--frame-light);
  }
  .pack-shapes{position:absolute;inset:0}
  .pack-title{position:absolute;left:70px;top:222px;color:var(--ink);font-family:"Libre Franklin",sans-serif}
  .pack-title .variant{display:block;font-size:56px;font-weight:700;line-height:1;padding-left:88px}
  .pack-title .product{display:block;font-size:136px;font-weight:900;line-height:.92;letter-spacing:-2px}
  .pack-title .claim{display:block;font-size:56px;font-weight:800;line-height:1.05;letter-spacing:1px}
  .nutrition{
    position:absolute;left:70px;top:490px;width:380px;
    font-family:"Roboto",sans-serif;font-weight:700;font-size:16.5px;line-height:1.32;color:var(--ink);
  }
  .emblems{position:absolute;left:488px;top:218px;list-style:none}
  .emblem{display:flex;align-items:center;height:133px;gap:14px}
  .emblem svg{width:56px;height:56px;flex:none}
  .emblem span{font-family:"Oswald",sans-serif;font-weight:600;font-size:37px;line-height:1.1;color:var(--ink);text-transform:uppercase}
  .net-weight{
    position:absolute;left:207px;top:1000px;width:281px;height:85px;
    display:flex;align-items:center;justify-content:center;
    font-family:"Roboto",sans-serif;font-weight:700;font-size:27px;color:var(--ink);
  }
</style>
</head>
<body>
<main class="pack" aria-label="Mellowgrain plain gluten free flour pack front">
  <svg class="pack-shapes" viewBox="0 0 775 1085" width="775" height="1085">
    <path class="saffron-panel" d="M520 0 C430 70 520 150 470 240 L470 1085 L775 1085 L775 0 Z" fill="var(--saffron)"/>
    <rect class="checker-area" x="0" y="520" width="470" height="150" fill="var(--checker)" role="img" aria-label="Decorative checkered band"/>
    <path class="charcoal-band" d="M0 630 C150 590 320 700 470 650 L470 1085 L0 1085 Z" fill="var(--charcoal)"/>
    <defs>
      <linearGradient id="grainTone" x1="0" y1="0" x2="1" y2="1">
        <stop offset="0" stop-color="#f3dfa8"/><stop offset="1" stop-color="var(--grain-gold)"/>
      </linearGradient>
      <radialGradient id="rotiTone" cx=".5" cy=".4" r=".6">
        <stop offset="0" stop-color="var(--roti-light)"/><stop offset="1" stop-color="var(--roti-dark)"/>
      </radialGradient>
    </defs>
    <rect class="grain-art" x="44" y="30" width="326" height="180" rx="20" fill="url(#grainTone)" opacity=".75" role="img" aria-label="Golden grain stalk illustration"/>
    <ellipse class="roti-photo" cx="220" cy="880" rx="165" ry="130" fill="url(#rotiTone)" role="img" aria-label="Photo of a stack of soft rotis"/>
    <path class="net-tab" d="M207 1085 L207 1030 Q207 1000 240 1000 L455 1000 Q488 1000 488 1030 L488 1085 Z" fill="var(--paper)"/>
  </svg>

  <h1 class="pack-title">
    <span class="variant">Plain</span>
    <span class="product">Flour</span>
    <span class="claim">GLUTEN FREE</span>
  </h1>

  <p class="nutrition">0% Saturated Fat only 1% Total fat, Cholesterol Free, Very Low Sodium, Good Source of Dietary Fiber. Weight management. Perfect for Gluten free lifestyle.</p>

  <ul class="emblems">
    <li class="emblem">
      <svg viewBox="0 0 56 56"><circle cx="28" cy="28" r="25" fill="none" stroke="var(--ink)" stroke-width="3"/><path d="M16 36 C18 20 32 14 42 16 C42 30 32 40 16 36 Z M16 36 L34 22" fill="var(--ink)" stroke="var(--saffron)" stroke-width="2"/></svg>
      <span>100%<br>Organic</span>
    </li>
    <li class="emblem">
      <svg viewBox="0 0 56 56"><circle cx="28" cy="28" r="25" fill="none" stroke="var(--ink)" stroke-width="3"/><path d="M28 14 L28 44" stroke="var(--ink)" stroke-width="3"/><g fill="var(--ink)"><ellipse cx="22" cy="22" rx="4" ry="6"/><ellipse cx="34" cy="22" rx="4" ry="6"/><ellipse cx="22" cy="33" rx="4" ry="6"/><ellipse cx="34" cy="33" rx="4" ry="6"/></g></svg>
      <span>100%<br>Gluten Free</span>
    </li>
    <li class="emblem">
      <svg viewBox="0 0 56 56"><rect x="6" y="6" width="44" height="44" rx="8" fill="none" stroke="var(--ink)" stroke-width="3"/><text x="28" y="26" text-anchor="middle" font-family="Oswald,sans-serif" font-size="13" font-weight="600" fill="var(--ink)">LOW</text><text x="28" y="42" text-anchor="middle" font-family="Oswald,sans-serif" font-size="13" font-weight="600" fill="var(--ink)">GI</text></svg>
      <span>Low GI</span>
    </li>
    <li class="emblem">
      <svg viewBox="0 0 56 56"><rect x="6" y="6" width="44" height="44" rx="8" fill="none" stroke="var(--ink)" stroke-width="3"/><path d="M16 18 L28 42 L40 18" fill="none" stroke="var(--ink)" stroke-width="4" stroke-linejoin="round"/></svg>
      <span>Vegan</span>
    </li>
    <li class="emblem">
      <svg viewBox="0 0 56 56"><circle cx="28" cy="28" r="25" fill="none" stroke="var(--ink)" stroke-width="3"/><ellipse cx="28" cy="28" rx="7" ry="12" fill="var(--ink)"/><path d="M12 12 L44 44" stroke="var(--ink)" stroke-width="3"/></svg>
      <span>Soy Free</span>
    </li>
    <li class="emblem">
      <svg viewBox="0 0 56 56"><rect x="6" y="6" width="44" height="44" rx="8" fill="none" stroke="var(--ink)" stroke-width="3"/><path d="M22 12 L34 12 L34 18 L38 24 L38 44 L18 44 L18 24 L22 18 Z" fill="var(--ink)"/></svg>
      <span>Dairy Free</span>
    </li>
  </ul>

  <p class="net-weight">NET WT: 500gm</p>
</main>
</body>
</html>
```